Meridel Haulage - Website

A clean, not cluttered informative website for our business. We specialize in the transportation of radioactive materials across North America. The site is mostly for information about our company and will not be used to attract business but will be used to attract employee's mainly drivers. Driver's are very hard to find in our area. One of the pages needs to be a job's posting page with an apply now button. Either an application can be filled out there or a resume can be uploaded which ever functionality works better. I would like a website that I can easily edit, ability to change text and photos.

Number of Pages Required

5+ page

Colors

Designer to choose colors to be used in the design.

Requirements
Must have
• Home - About - Services - Jobs - Contact pages
• A way prospective employee's can apply or upload their resume to be emailed to me
• Very clean apperance
Should not have
• I don't want it to be busy

```html
<!DOCTYPE html>
<html lang="en">
<head>
<meta charset="utf-8">
<title>Meridel Haulage – Jobs</title>
<link rel="stylesheet" href="https://fonts.googleapis.com/css2?family=Figtree:ital,wght@0,400;0,500;0,600;1,400&display=swap">
<style>
  :root {
    --page-bg: #ebebeb;
    --map-tone: #dcdcdc;
    --card: #ffffff;
    --ink: #1d1d1f;
    --muted: #8a8a8a;
    --brand: #1a6fbf;
    --rail: #77787b;
  }
  * { box-sizing: border-box; margin: 0; padding: 0; }
  html, body { width: 1200px; height: 800px; overflow: hidden; }
  body {
    position: relative;
    background: var(--page-bg);
    font-family: "Figtree", "Helvetica Neue", Arial, sans-serif;
    color: var(--ink);
  }
  .map-backdrop {
    position: absolute; left: 110px; top: 80px; width: 1040px; height: 640px;
    background: radial-gradient(ellipse at 50% 45%, var(--map-tone) 0%, rgba(220,220,220,0.5) 45%, rgba(235,235,235,0) 72%);
  }
  .site-header { position: absolute; left: 0; top: 0; width: 1200px; height: 90px; }
  .brand {
    position: absolute; left: 136px; top: 28px;
    display: flex; align-items: center; gap: 8px;
    font-size: 22px; font-weight: 600; color: var(--brand); letter-spacing: 0.5px;
  }
  .brand-mark { width: 14px; height: 14px; background: var(--brand); }
  .main-nav { position: absolute; top: 39px; left: 0; }
  .main-nav a {
    position: absolute; white-space: nowrap; text-decoration: none;
    font-size: 11px; letter-spacing: 3.2px; color: #3a3a3a;
  }
  .main-nav a.is-active { color: var(--brand); font-weight: 600; }
  .job-list { position: absolute; left: 282px; top: 138px; width: 636px; }
  .job {
    position: relative; background: var(--card); border-left: 6px solid var(--rail);
    height: 38px; margin-bottom: 8px;
  }
  .job-title { position: absolute; left: 18px; top: 11px; font-size: 14px; font-weight: 400; }
  .job-place { position: absolute; left: 346px; top: 10px; width: 72px; text-align: center; font-size: 14px; font-style: italic; }
  .toggle { position: absolute; right: 18px; top: 12px; width: 14px; height: 14px; }
  .job.is-open { height: 328px; border-left-color: var(--brand); }
  .job.is-open .job-title { font-weight: 500; }
  .job-body { position: absolute; left: 19px; top: 60px; width: 298px; font-size: 10px; line-height: 16px; color: #2a2a2a; }
  .job-body p + p { margin-top: 16px; }
  .job-facts { position: absolute; left: 364px; top: 60px; width: 226px; }
  .fact-label { font-size: 8.5px; letter-spacing: 2.4px; color: var(--muted); }
  .fact-value { font-size: 10px; font-style: italic; margin: 3px 0 14px 8px; color: #333; }
  .fact-list { list-style: none; font-size: 10px; font-style: italic; line-height: 13.5px; margin-top: 4px; color: #333; }
  .apply-btn {
    display: flex; justify-content: space-between; align-items: center;
    margin-top: 27px; width: 226px; height: 38px; padding: 0 20px 0 19px;
    background: var(--brand); color: #fff; font-size: 14px; text-decoration: none;
  }
  .footer-band { position: absolute; left: 0; bottom: 0; width: 1200px; height: 8px; background: var(--brand); }
</style>
</head>
<body>
  <div class="map-backdrop" role="img" aria-label="Faint dotted map of North America"></div>

  <header class="site-header">
    <div class="brand"><span class="brand-mark"></span>Meridel Haulage</div>
    <nav class="main-nav">
      <a class="is-active" href="#" style="left:666px">JOBS</a>
      <a href="#" style="left:754px">SERVICES</a>
      <a href="#" style="left:877px">ABOUT</a>
      <a href="#" style="left:965px">CONTACT</a>
    </nav>
  </header>

  <main class="job-list">
    <article class="job">
      <h2 class="job-title">Truck driver</h2><span class="job-place">Otawa, ON</span>
      <svg class="toggle" viewBox="0 0 14 14"><path d="M7 0v14M0 7h14" stroke="#1a6fbf" stroke-width="1.5"/></svg>
    </article>
    <article class="job">
      <h2 class="job-title" style="left:16px">Warehouse superviser</h2><span class="job-place">Perth, ON</span>
      <svg class="toggle" viewBox="0 0 14 14"><path d="M7 0v14M0 7h14" stroke="#1a6fbf" stroke-width="1.5"/></svg>
    </article>
    <article class="job">
      <h2 class="job-title" style="left:19px">Truck driver</h2><span class="job-place">Otawa, ON</span>
      <svg class="toggle" viewBox="0 0 14 14"><path d="M7 0v14M0 7h14" stroke="#1a6fbf" stroke-width="1.5"/></svg>
    </article>
    <article class="job">
      <h2 class="job-title" style="left:19px">Salesman</h2><span class="job-place">Perth, ON</span>
      <svg class="toggle" viewBox="0 0 14 14"><path d="M7 0v14M0 7h14" stroke="#1a6fbf" stroke-width="1.5"/></svg>
    </article>
    <article class="job is-open">
      <h2 class="job-title">Truck driver</h2>
      <svg class="toggle" viewBox="0 0 14 14"><path d="M3 7h8" stroke="#1a6fbf" stroke-width="1.5"/></svg>
      <div class="job-body">
        <p>Lorem ipsum dolor sit amet, consectetur adipiscing elit. Proin feugiat sem vel sem luctus vulputate. Suspendisse rhoncus consequat consequat. Donec dolor magna, blandit non odio eleifend, rutrum faucibus mi. Duis vitae erat et elit venenatis elementum nec in velit. Sed ante lectus, euismod sit amet nibh eu, tristique pretium tellus. Interdum et malesuada fames ac ante ipsum primis in faucibus.</p>
        <p>Donec dictum sollicitudin nisi, pellentesque fermentum massa blandit ac. Sed a fermentum tortor. Etiam vel nibh a mauris placerat imperdiet eu in mi. Suspendisse faucibus massa vitae pulvinar iaculis. Morbi sit amet mi nisi. Nunc porta maximus velit quis accumsan. Pellentesque hendrerit ex ut tellus efficitur pharetra. Sed auctor aliquam faucibus.</p>
      </div>
      <aside class="job-facts">
        <div class="fact-label">LOCATION:</div>
        <div class="fact-value">Perth, ON</div>
        <div class="fact-label">POSITION:</div>
        <div class="fact-value">Full-time</div>
        <div class="fact-label">REQUIREMENTS:</div>
        <ul class="fact-list">
          <li>- Truck license</li>
          <li>- 5 year expieriance</li>
          <li>- something else</li>
          <li>- something more</li>
        </ul>
        <a class="apply-btn" href="#"><span>Apply for a Job</span><span>&gt;&gt;</span></a>
      </aside>
    </article>
    <article class="job">
      <h2 class="job-title" style="left:19px">Salesman</h2><span class="job-place">Perth, ON</span>
      <svg class="toggle" viewBox="0 0 14 14"><path d="M7 0v14M0 7h14" stroke="#1a6fbf" stroke-width="1.5"/></svg>
    </article>
  </main>

  <div class="footer-band"></div>
</body>
</html>
```